Torvel Law, PC Letterhead Design -- LAW FIRM

I am looking for a very elegant letterhead design for my personal injury law practice.
The letter head must have 4 different variations of the same thing meaning one design that has just a header, and another with a header and footer.
Elegance is key, I do not want it to be too bold. Please stay away from colors that are not black, white or gray or silver.
Please include a gradient style letterhead for the header while implementing the design of the logo found in folder #3
I have attached for you the logos and emblems for my company below.
In folders 1-4 you will find my actual logo.
In folder 5-6 you will find a shorter version of my logo, this can be implemented maybe in the footer + header design of the letter head (do not include this shortened version in the header).
In folders 7-8 you will find an emblem for my company.
Information that needs to be found on the letterhead is as follows:
A clearly written version of my company name: Torvel Law, PC
Address: 4718 Pemberly Avenue Suite #512, Beverly Hills, CA, 90210
Email: dorian@torvellaw.example
Telephone number: 310-555-0174

```html
<!DOCTYPE html>
<html lang="en">
<head>
<meta charset="utf-8">
<title>Torvel Law, PC — Letterhead and Envelope</title>
<link rel="stylesheet" href="https://fonts.googleapis.com/css2?family=Open+Sans:wght@400;600&display=swap">
<style>
  :root {
    --backdrop: #e9e9ea;
    --paper: #fbfbfb;
    --ink: #1b1b1c;
    --text: #4a4a4c;
    --muted: #8a8a8c;
    --faint: #d6d6d8;
    --band: #1a1a1b;
    --white: #ffffff;
  }
  * { box-sizing: border-box; margin: 0; padding: 0; }
  html, body {
    width: 1200px; height: 795px; overflow: hidden;
    background: var(--backdrop);
    font-family: "Open Sans", Arial, sans-serif;
  }
  .canvas { position: relative; width: 1200px; height: 795px; }

  /* Letterhead */
  .letterhead {
    position: absolute; left: 70px; top: 28px;
    width: 524px; height: 740px;
    background: var(--paper);
    box-shadow: 0 2px 10px rgba(0,0,0,.08);
    overflow: hidden;
    padding: 56px 48px 0 52px;
    color: var(--text);
  }
  .letterhead-header { position: relative; height: 96px; }
  .firm-name {
    position: absolute; left: 120px; top: 22px;
    font-size: 22px; font-weight: 400; letter-spacing: .5px;
    color: var(--ink);
  }
  .contact {
    position: absolute; right: 0; top: 58px;
    font-size: 7.5px; font-weight: 600; line-height: 1.5;
    text-align: left; color: var(--text);
  }
  .contact-line { display: flex; align-items: center; gap: 4px; }
  .contact-line svg { width: 7px; height: 7px; fill: var(--text); }
  .salutation { font-size: 8px; margin: 6px 0 10px; }
  .body-copy p {
    font-size: 8px; line-height: 1.55; margin-bottom: 10px;
    text-indent: 14px;
  }
  .closing { font-size: 8px; margin-top: 4px; }
  .signature {
    width: 70px; height: 36px; margin-top: 12px;
    background: linear-gradient(135deg, #eaeaeb, #dcdcdd);
    border-radius: 3px;
  }
  .watermark {
    position: absolute; left: 30px; bottom: 40px;
    font-size: 86px; font-weight: 400; color: var(--faint);
    letter-spacing: 1px; white-space: nowrap;
  }

  /* Envelope */
  .envelope {
    position: absolute; left: 628px; top: 300px;
    width: 520px; height: 270px;
    background: var(--paper);
    box-shadow: 0 2px 10px rgba(0,0,0,.08);
  }
  .envelope-flap {
    position: absolute; left: 0; top: 0; width: 100%; height: 112px;
    background: var(--band);
    border-radius: 0 0 16px 16px;
    display: flex; align-items: center; justify-content: center; gap: 12px;
  }
  .flap-mark {
    width: 44px; height: 44px; border-radius: 50%;
    background: var(--white);
  }
  .flap-name {
    font-size: 15px; font-weight: 400; color: var(--white); letter-spacing: .5px;
  }
</style>
</head>
<body>
<main class="canvas">

  <section class="letterhead" aria-label="Letterhead">
    <header class="letterhead-header">
      <div class="firm-name">Torvel Law, PC</div>
      <address class="contact" style="font-style:normal">
        <div>4718 Pemberly Avenue Suite</div>
        <div>#512, Beverly Hills, CA, 90210</div>
        <div class="contact-line">
          <svg viewBox="0 0 10 10" aria-hidden="true"><path d="M2 0.5 L4 3 L3 4 Q4.5 6 6 7 L7 6 L9.5 8 L8.5 9.5 Q4 9 0.5 1.5 Z"/></svg>
          <span>310-555-0174</span>
        </div>
        <div class="contact-line">
          <svg viewBox="0 0 10 10" aria-hidden="true"><path d="M0 2 H10 V8 H0 Z M0.6 2.4 L5 5.6 L9.4 2.4" /></svg>
          <span>dorian@torvellaw.example</span>
        </div>
      </address>
    </header>

    <p class="salutation">Dear customer,</p>
    <div class="body-copy">
      <p>Lorem ipsum dolor sit amet, consectetur adipisicing elit, sed do eiusmod tempor incididunt ut labore et dolore magna aliqua. Ut enim ad minim veniam, quis nostrud exercitation ullamco laboris nisi ut aliquip ex ea commodo consequat. Duis aute irure dolor in reprehenderit in voluptate velit esse cillum dolore eu fugiat nulla pariatur. Excepteur sint occaecat cupidatat non proident, sunt in culpa qui officia deserunt mollit anim id est laborum.</p>
      <p>Lorem ipsum dolor sit amet, consectetur adipisicing elit, sed do eiusmod tempor incididunt ut labore et dolore magna aliqua. Ut enim ad minim veniam, quis nostrud exercitation ullamco laboris nisi ut aliquip ex ea commodo consequat. Duis aute irure dolor in reprehenderit in voluptate velit esse cillum dolore eu fugiat nulla pariatur. Excepteur sint occaecat cupidatat non proident, sunt in culpa qui officia deserunt mollit anim id est laborum.</p>
      <p>Lorem ipsum dolor sit amet, consectetur adipisicing elit, sed do eiusmod tempor incididunt ut labore et dolore magna aliqua. Ut enim ad minim veniam, quis nostrud exercitation ullamco laboris nisi ut aliquip ex ea commodo consequat. Duis aute irure dolor in reprehenderit in voluptate velit esse cillum dolore eu fugiat nulla pariatur. Excepteur sint occaecat cupidatat non proident, sunt in culpa qui officia deserunt mollit anim id est laborum.</p>
      <p>Lorem ipsum dolor sit amet, consectetur adipisicing elit, sed do eiusmod tempor incididunt ut labore et dolore magna aliqua. Ut enim ad minim veniam, quis nostrud exercitation ullamco laboris nisi ut aliquip ex ea commodo consequat. Duis aute irure dolor.</p>
    </div>
    <p class="closing">Yours Sincerely,</p>
    <div class="signature" role="img" aria-label="Handwritten signature of the sender"></div>

    <div class="watermark" aria-hidden="true">Torvel Law</div>
  </section>

  <section class="envelope" aria-label="Envelope back">
    <div class="envelope-flap">
      <span class="flap-mark" aria-hidden="true"></span>
      <span class="flap-name">Torvel Law</span>
    </div>
  </section>

</main>
</body>
</html>
```